Company Holiday E-Card Template

Company holiday e-card template in PPT or another format that can be customized. This card will contain 6 images and 1-2 lines of copy. We would like 2 different design options corresponding with the images attached. For the Tree, please have spaces for 6 images. One on top, two in the middle and three on the bottom. Copy on the Bottom (please allow this to be customize-able as it may change): Happy Holiday's from BRT!We look forward to great things in 2019!For the tags design: I need to put photos where the hang-tags are currently placed. Also copy on the bottom "'Happy Holiday's from BRT"I will need to be able to customize this as we may need to add more photos, etc... so please provide a template that can be updated. PPT would be ideal. Need spaces for 6 images total. I need to be able to insert the images into the corresponding spaces. Copy to be included: Happy Holiday's from BRT!

Font styles to use
Serif

Requirements
Must have
• Customizable template design to hold 6 images and copy.

```html
<!DOCTYPE html>
<html lang="en">
<head>
<meta charset="utf-8">
<title>Holiday E-Card – BRT</title>
<link rel="stylesheet" href="https://fonts.googleapis.com/css2?family=Crimson+Text&display=swap">
<style>
  :root {
    --page: #ffffff;
    --card-red: #e01e35;
    --band-blue: #00a9e4;
    --star-blue: #4cb8e6;
    --frame-peach: #f8c3ab;
    --photo-gold: #ccb05f;
    --greeting-red: #e8202f;
  }
  html, body {
    margin: 0;
    padding: 0;
    width: 849px;
    height: 1200px;
    overflow: hidden;
    background: var(--page);
  }
  .canvas {
    position: relative;
    width: 849px;
    height: 1200px;
  }
  .card {
    position: absolute;
    left: 96px;
    top: 156px;
    width: 645px;
    height: 908px;
    border-radius: 36px;
    background: var(--card-red);
    overflow: hidden;
  }
  .tree-star {
    position: absolute;
    left: 376px;
    top: 174px;
    width: 84px;
    height: 84px;
  }
  .photo-frame {
    position: absolute;
    width: 181px;
    height: 181px;
    box-sizing: border-box;
    border: 11px solid var(--frame-peach);
    background: var(--photo-gold);
    box-shadow: 0 4px 10px rgba(80, 0, 10, 0.45);
  }
  .photo-top        { left: 331px; top: 282px; z-index: 4; }
  .photo-mid-left   { left: 232px; top: 467px; z-index: 3; transform: rotate(-2deg); }
  .photo-mid-right  { left: 418px; top: 467px; z-index: 3; transform: rotate(2deg); }
  .photo-low-left   { left: 146px; top: 644px; z-index: 1; transform: rotate(-1deg); }
  .photo-low-center { left: 331px; top: 648px; z-index: 2; }
  .photo-low-right  { left: 512px; top: 644px; z-index: 1; }
  .greeting-band {
    position: absolute;
    left: 0;
    bottom: 0;
    width: 100%;
    height: 90px;
    background: var(--band-blue);
    box-shadow: 0 -6px 10px rgba(60, 0, 10, 0.55);
    display: flex;
    align-items: center;
    justify-content: center;
  }
  .greeting-text {
    margin: 0;
    font-family: "Crimson Text", Georgia, serif;
    font-weight: 400;
    font-size: 43px;
    color: var(--greeting-red);
    letter-spacing: 0.3px;
  }
</style>
</head>
<body>
<main class="canvas">
  <section class="card">
    <div class="greeting-band">
      <p class="greeting-text">Happy Holiday's from BRT</p>
    </div>
  </section>

  <svg class="tree-star" viewBox="0 0 100 100" aria-hidden="true">
    <path d="M50 5 L61 37 L95 38 L68 58 L78 92 L50 72 L22 92 L32 58 L5 38 L39 37 Z"
          fill="var(--star-blue)" stroke="var(--star-blue)" stroke-width="6" stroke-linejoin="round"/>
  </svg>

  <div class="photo-frame photo-top" role="img" aria-label="Photo space 1"></div>
  <div class="photo-frame photo-mid-left" role="img" aria-label="Photo space 2"></div>
  <div class="photo-frame photo-mid-right" role="img" aria-label="Photo space 3"></div>
  <div class="photo-frame photo-low-left" role="img" aria-label="Photo space 4"></div>
  <div class="photo-frame photo-low-center" role="img" aria-label="Photo space 5"></div>
  <div class="photo-frame photo-low-right" role="img" aria-label="Photo space 6"></div>
</main>
</body>
</html>
```